Hearth Table Cover Design

Open to creative ideas, we don't have a set cover style in mind so have fun with it!
Front Cover for Ebook-Quorvex and vantor shelf. Book title is "Hearth Table" sub title is "A Gentle Map for Kitchen Rhythms", Author is Corinne L Waddell. Website is www.theolwynkitchenworks.com.
Open to creative ideas, we dont' have a set cover style in mind so have fun with it!
We have attached some pictures of Corinne which could be incorporated into the title. We can send you high def files if you need.
We have attached two book covers which we like to get you started, but feel free to have fun, we're looking for something creative and catchy

```html
<!DOCTYPE html>
<html lang="en">
<head>
<meta charset="utf-8">
<title>Hearth Table — Cover</title>
<link href="https://fonts.googleapis.com/css2?family=Questrial&display=swap" rel="stylesheet">
<style>
  :root {
    --stage: #000000;
    --band-orange: #e0490f;
    --title-white: #ffffff;
    --subtitle-brown: #4a1a06;
    --author-ink: #111111;
    --author-veil: rgba(255, 255, 255, 0.6);
    --sky-light: #fefcf8;
    --bark-light: #f0cfae;
    --bark-mid: #dba784;
    --bark-deep: #c98f6c;
    --hair-blonde: #e9c590;
    --skin-warm: #eebf9f;
    --shirt-sage: #7f9a84;
    --glow-peach: #f6b870;
  }
  html, body {
    margin: 0;
    padding: 0;
    width: 1000px;
    height: 1200px;
    overflow: hidden;
    background: var(--stage);
  }
  .canvas {
    position: relative;
    width: 1000px;
    height: 1200px;
    background: var(--stage);
  }
  .cover {
    position: absolute;
    left: 152px;
    top: 75px;
    width: 710px;
    height: 1063px;
    overflow: hidden;
    background: var(--sky-light);
  }
  .tree-trunk {
    position: absolute;
    left: 0;
    top: 0;
    width: 190px;
    height: 1063px;
    background: linear-gradient(90deg, var(--bark-deep) 0%, var(--bark-mid) 45%, var(--bark-light) 100%);
  }
  .author-portrait {
    position: absolute;
    left: 175px;
    top: 45px;
    width: 500px;
    height: 1018px;
    border-radius: 220px 220px 0 0;
    background: linear-gradient(180deg,
      var(--hair-blonde) 0%,
      var(--skin-warm) 30%,
      var(--hair-blonde) 48%,
      var(--shirt-sage) 58%,
      var(--shirt-sage) 78%,
      var(--glow-peach) 100%);
  }
  .warm-glow {
    position: absolute;
    inset: 0;
    background:
      radial-gradient(circle at 80% 100%, rgba(246,184,112,0.75) 0%, rgba(246,184,112,0) 45%),
      radial-gradient(circle at 10% 0%, rgba(255,236,190,0.55) 0%, rgba(255,236,190,0) 35%);
  }
  .cover-type {
    position: absolute;
    inset: 0;
    width: 710px;
    height: 1063px;
    font-family: "Questrial", "Century Gothic", sans-serif;
  }
  .title-band { fill: var(--band-orange); }
  .book-title { fill: var(--title-white); font-size: 86px; }
  .book-subtitle { fill: var(--subtitle-brown); font-size: 40px; }
  .author-veil { fill: var(--author-veil); }
  .author-name { fill: var(--author-ink); font-size: 36px; }
</style>
</head>
<body>
<main class="canvas">
  <section class="cover">
    <div class="tree-trunk" role="img" aria-label="Pale, mottled tree trunk on the left edge of the photo"></div>
    <div class="author-portrait" role="img" aria-label="Photograph of the author with long blonde hair and a sage green t-shirt, smiling and leaning on the tree"></div>
    <div class="warm-glow"></div>
    <svg class="cover-type" viewBox="0 0 710 1063" xmlns="http://www.w3.org/2000/svg">
      <g transform="translate(0 905) rotate(-21)">
        <rect class="author-veil" x="170" y="-122" width="620" height="58"/>
        <text class="author-name" x="215" y="-78">Corinne L Waddell</text>
        <rect class="title-band" x="-80" y="-60" width="900" height="122"/>
        <text class="book-title" x="12" y="32">Hearth Table</text>
        <text class="book-subtitle" x="30" y="104">A Gentle Map for Kitchen Rhythms</text>
      </g>
    </svg>
  </section>
</main>
</body>
</html>
```